New minimal and cool business card

We have a brand new logo - we would like to use the logo on blue on the front of the card
The tagline is The give and take network (tm)
We would like information on the back of the card for individual(s)

Our font is Lato
Our colors are indicated in the attached identity guide which uses the old logo - we are de-emphasizing orange

Please prepare the artwork to meet the specs on this site
http://us.prinvo.com/products/velora/business-cards.html

Front: Logo and tagline on dark blue

Back: On white
Join Today
http://zentaro.co/join

```html
<!DOCTYPE html>
<html lang="en">
<head>
<meta charset="utf-8">
<title>Zentaro Business Card</title>
<link href="https://fonts.googleapis.com/css2?family=Lato:wght@400;700&display=swap" rel="stylesheet">
<style>
  :root {
    --navy: #2f4259;
    --navy-deep: #283a4f;
    --card-white: #f8f8f8;
    --ink: #3a3f45;
    --muted: #6c7078;
    --stage: #ebe8e2;
  }
  * { margin: 0; padding: 0; box-sizing: border-box; }
  html, body { width: 1200px; height: 989px; overflow: hidden; }
  body {
    background: var(--stage);
    font-family: "Lato", sans-serif;
    position: relative;
  }
  .card {
    position: absolute;
    top: 345px;
    width: 520px;
    height: 298px;
    border-radius: 18px;
    box-shadow: 0 6px 18px rgba(0,0,0,0.15);
  }
  .card-back { left: 60px; background: var(--card-white); }
  .card-front { left: 620px; background: var(--navy); }

  .brand {
    position: absolute;
    left: 44px;
    top: 92px;
    color: var(--navy);
    font-weight: 700;
    font-size: 40px;
    letter-spacing: 0.5px;
    line-height: 1;
  }
  .brand-tm { font-size: 10px; vertical-align: top; margin-left: 2px; }
  .brand-stage {
    display: block;
    text-align: right;
    font-size: 9px;
    letter-spacing: 4px;
    font-weight: 400;
    color: var(--navy);
    margin-top: 4px;
  }
  .person { position: absolute; left: 44px; top: 168px; }
  .person-name { font-weight: 700; font-size: 16px; color: var(--navy); }
  .person-role { font-size: 11px; color: var(--muted); margin-top: 2px; }
  .contact {
    position: absolute;
    left: 44px;
    top: 212px;
    font-size: 11px;
    color: var(--ink);
    line-height: 15px;
    list-style: none;
  }
  .contact li { display: flex; align-items: center; gap: 5px; }
  .contact svg { width: 9px; height: 9px; }

  .join { position: absolute; right: 40px; top: 40px; text-align: right; }
  .join-title { font-weight: 700; font-size: 16px; color: var(--navy); }
  .join-link {
    display: inline-block;
    margin-top: 8px;
    background: var(--navy);
    color: #dfe5ec;
    font-size: 10px;
    padding: 9px 18px;
    border-radius: 8px;
  }

  .front-brand {
    position: absolute;
    left: 0; right: 0;
    top: 122px;
    text-align: center;
    color: #ffffff;
    font-weight: 700;
    font-size: 54px;
    letter-spacing: 1px;
    line-height: 1;
  }
  .front-brand .brand-tm { font-size: 11px; }
</style>
</head>
<body>
  <section class="card card-back">
    <div class="brand">zentaro<span class="brand-tm">TM</span><span class="brand-stage">BETA</span></div>
    <div class="person">
      <p class="person-name">Marlo Vance</p>
      <p class="person-role">Director</p>
    </div>
    <ul class="contact">
      <li>Suite 000 Harbour Road</li>
      <li>Westbrook NSW 2000</li>
      <li>PO BOX 000</li>
      <li><svg viewBox="0 0 10 10"><rect width="10" height="10" rx="1" fill="#2f4259"/><path d="M3 2h1.5l.5 2-1 .7a5 5 0 0 0 1.8 1.8l.7-1 2 .5V8a1 1 0 0 1-1 1A5.5 5.5 0 0 1 2 3a1 1 0 0 1 1-1z" fill="#fff"/></svg>0400 000 123</li>
      <li><svg viewBox="0 0 10 10"><rect width="10" height="10" rx="1" fill="#2f4259"/><rect x="2" y="3" width="6" height="4.2" fill="none" stroke="#fff" stroke-width="0.8"/><path d="M2 3l3 2.3L8 3" fill="none" stroke="#fff" stroke-width="0.8"/></svg>marlo@zentaro.co</li>
    </ul>
    <div class="join">
      <p class="join-title">Join Today</p>
      <p class="join-link">www.zentaro.co/join</p>
    </div>
  </section>

  <section class="card card-front">
    <div class="front-brand">zentaro<span class="brand-tm">TM</span></div>
  </section>
</body>
</html>
```